Construction Business Card Design

We have a landscape construction company based in Australia
Were out of business cards ,
So now we're after a fresh looking modern card to give a fresh look to our business ....
We would like the business card to have the
(Front)
Tallow Ridge Pty Ltd
Director Norman Cusk
0462395108
(Back)
Landscape,Construction,Paving,Excavation
(In smaller font low in the frame of card)
Different textures , curved edge , vertical and horizontal designs also minimal colours per design
Eg one side black , one coloured or a splash here or there
Industry/Entity Type
Landscape
Contact Information for Business Card
Tallow Ridge Pty Ltd
Director Norman Cusk
0462395108
Landscape,Paving,Construction,Excavation
Look and feel

```html
<!DOCTYPE html>
<html lang="en">
<head>
<meta charset="utf-8">
<title>Tallow Ridge Pty Ltd — Business Cards</title>
<link rel="stylesheet" href="https://fonts.googleapis.com/css2?family=Fira+Sans:wght@400;500&display=swap">
<style>
  :root {
    --page: #c9c9c9;
    --card: #101010;
    --card-edge: #1c1c1c;
    --green: #7cc242;
    --blue: #27aae1;
    --white: #f2f2f2;
  }
  * { box-sizing: border-box; margin: 0; padding: 0; }
  html, body {
    width: 1200px;
    height: 1037px;
    overflow: hidden;
    background: var(--page);
    font-family: "Fira Sans", sans-serif;
  }
  .sheet {
    position: relative;
    width: 1200px;
    height: 1037px;
  }
  .card {
    position: absolute;
    top: 128px;
    width: 440px;
    height: 780px;
    background: radial-gradient(ellipse at 50% 30%, var(--card-edge) 0%, var(--card) 70%);
    overflow: hidden;
    box-shadow: 0 18px 40px rgba(0,0,0,0.35);
  }
  .card--back {
    left: 130px;
    border-radius: 70px 0 70px 0;
  }
  .card--front {
    left: 630px;
    border-radius: 0 70px 0 70px;
  }
  .card__rules {
    position: absolute;
    inset: 0;
    width: 100%;
    height: 100%;
  }
  .services {
    position: absolute;
    left: 110px;
    top: 215px;
    list-style: none;
    color: var(--white);
    font-size: 27px;
    font-weight: 400;
    letter-spacing: 0.3px;
  }
  .services li { height: 63px; }
  .texture {
    position: absolute;
    inset: 0;
    background:
      radial-gradient(ellipse at 55% 35%, rgba(60,60,60,0.55) 0%, rgba(20,20,20,0) 65%),
      linear-gradient(160deg, #1d1d1d 0%, #0c0c0c 100%);
  }
  .contact {
    position: absolute;
    left: 58px;
    top: 150px;
  }
  .contact__name {
    color: var(--green);
    font-size: 32px;
    font-weight: 400;
    letter-spacing: 0.5px;
  }
  .contact__role {
    color: var(--blue);
    font-size: 17px;
    margin-top: 2px;
  }
  .contact__phone {
    color: var(--blue);
    font-size: 28px;
    letter-spacing: 1px;
    margin-top: 2px;
  }
  .brand {
    position: absolute;
    right: 48px;
    bottom: 78px;
    text-align: right;
    color: var(--blue);
    font-weight: 500;
    line-height: 1;
  }
  .brand__name { font-size: 54px; letter-spacing: -0.5px; }
  .brand__suffix { font-size: 30px; margin-top: 6px; }
</style>
</head>
<body>
<main class="sheet">

  <section class="card card--back" aria-label="Card back: services">
    <svg class="card__rules" viewBox="0 0 440 780" aria-hidden="true">
      <defs>
        <linearGradient id="rule-vertical" x1="0" y1="0" x2="0" y2="1">
          <stop offset="0" stop-color="#7cc242"/>
          <stop offset="1" stop-color="#27aae1"/>
        </linearGradient>
        <linearGradient id="rule-horizontal" x1="0" y1="0" x2="1" y2="0">
          <stop offset="0" stop-color="#7cc242"/>
          <stop offset="1" stop-color="#27aae1"/>
        </linearGradient>
      </defs>
      <g stroke="url(#rule-vertical)" stroke-width="3">
        <line x1="40" y1="120" x2="40" y2="780"/>
        <line x1="51" y1="132" x2="51" y2="780"/>
        <line x1="62" y1="144" x2="62" y2="780"/>
      </g>
      <g stroke="url(#rule-horizontal)" stroke-width="3">
        <line x1="0" y1="712" x2="420" y2="694"/>
        <line x1="0" y1="723" x2="420" y2="705"/>
        <line x1="0" y1="734" x2="420" y2="716"/>
      </g>
    </svg>
    <ul class="services">
      <li>Landscape</li>
      <li>Construction</li>
      <li>Concrete</li>
      <li>Carpentry</li>
      <li>Paving</li>
      <li>Pools</li>
      <li>Excavation</li>
      <li>Maintenance</li>
    </ul>
  </section>

  <section class="card card--front" aria-label="Card front: contact">
    <div class="texture" role="img" aria-label="Fine scattered crossing-line texture in dark grey"></div>
    <div class="contact">
      <p class="contact__name">Norman Cusk</p>
      <p class="contact__role">Director</p>
      <p class="contact__phone">0462395108</p>
    </div>
    <div class="brand">
      <p class="brand__name">Tallow Ridge</p>
      <p class="brand__suffix">Pty Ltd</p>
    </div>
  </section>

</main>
</body>
</html>
```